Sleek, Professional Business Card Design Needed

Business Cards - Logo Attached.

We are a solar consulting company. We are national and want our cards to represent the professional high quality products that we offer.

Industry/Entity Type

Business

Contact Information for Business Card

n/a

Requirements
Must have
• Design
• Name
• Position
• Number
• Email
• Address
Should not have
• Not be too crowded

```html
<!DOCTYPE html>
<html lang="en">
<head>
<meta charset="utf-8">
<title>Bright Field Solar – Business Card</title>
<link href="https://fonts.googleapis.com/css2?family=Lato:wght@300;400;700&display=swap" rel="stylesheet">
<style>
  :root {
    --stage: #2b2b2b;
    --brand-blue: #1b9bd7;
    --brand-blue-deep: #1488c2;
    --brand-green: #8cc63f;
    --paper: #ffffff;
    --paper-shade: #f0f0f0;
    --ink-grey: #6d6e71;
    --faint: rgba(255,255,255,0.08);
  }
  * { margin: 0; padding: 0; box-sizing: border-box; }
  html, body { width: 1200px; height: 1031px; overflow: hidden; }
  body {
    background: var(--stage);
    font-family: 'Lato', sans-serif;
    display: flex;
    flex-direction: column;
    align-items: center;
    justify-content: center;
    gap: 64px;
  }
  .card {
    position: relative;
    width: 640px;
    height: 366px;
    border-radius: 4px;
    overflow: hidden;
    box-shadow: 0 14px 30px rgba(0,0,0,0.45);
  }

  /* Front */
  .card--front {
    background: linear-gradient(160deg, var(--brand-blue) 0%, var(--brand-blue-deep) 100%);
    color: var(--paper);
  }
  .card--front .bg-ring {
    position: absolute;
    left: -90px; top: 60px;
    width: 420px; height: 420px;
    border-radius: 50%;
    border: 60px solid var(--faint);
  }
  .brand {
    display: flex;
    align-items: center;
    gap: 14px;
  }
  .brand__dot {
    width: 38px; height: 38px;
    border-radius: 50%;
    border: 5px solid currentColor;
  }
  .brand__name {
    font-size: 30px;
    font-weight: 400;
    letter-spacing: 1px;
    text-transform: uppercase;
    padding-bottom: 6px;
    border-bottom: 2px solid currentColor;
    line-height: 1.1;
  }
  .card--front .brand {
    position: absolute;
    right: 70px; top: 118px;
  }

  /* Back */
  .card--back {
    background: linear-gradient(135deg, var(--paper) 40%, var(--paper-shade) 100%);
  }
  .card--back .bg-ring {
    position: absolute;
    right: -40px; top: -160px;
    width: 420px; height: 420px;
    border-radius: 50%;
    border: 60px solid rgba(0,0,0,0.035);
  }
  .corner-dot {
    position: absolute;
    right: -22px; top: -22px;
    width: 56px; height: 56px;
    border-radius: 50%;
    background: var(--brand-blue);
  }
  .edge-tab {
    position: absolute;
    left: 0; bottom: 0;
    width: 14px; height: 104px;
    background: var(--brand-green);
    border-radius: 0 6px 0 0;
  }
  .card--back .brand {
    position: absolute;
    left: 44px; top: 44px;
    color: var(--brand-blue);
  }
  .card--back .brand__dot { border-color: var(--brand-green); }
  .card--back .brand__name {
    font-size: 26px;
    border-bottom-color: var(--brand-green);
  }
  .divider {
    position: absolute;
    left: 320px; top: 150px;
    width: 1px; height: 170px;
    background: var(--brand-green);
  }
  .person {
    position: absolute;
    right: 44px; top: 54px;
    text-align: right;
  }
  .person__name {
    color: var(--brand-blue);
    font-size: 26px;
    font-weight: 700;
    text-transform: uppercase;
    letter-spacing: 0.5px;
  }
  .person__role {
    color: var(--brand-green);
    font-size: 17px;
    font-weight: 400;
    margin-top: 2px;
  }
  .person__rule {
    width: 60px; height: 3px;
    background: var(--brand-blue);
    margin: 10px 0 0 auto;
  }
  .contact {
    position: absolute;
    left: 44px; bottom: 40px;
    list-style: none;
    color: var(--brand-blue);
    font-size: 15px;
    line-height: 1.55;
  }
  .contact li { display: flex; align-items: center; gap: 8px; }
  .contact .addr { text-transform: uppercase; letter-spacing: 0.4px; }
  .contact svg { width: 13px; height: 13px; flex: none; }
  .website {
    position: absolute;
    right: 44px; bottom: 40px;
    display: flex; align-items: center; gap: 8px;
    color: var(--brand-blue);
    font-size: 15px;
  }
  .website svg { width: 14px; height: 14px; }
</style>
</head>
<body>

  <section class="card card--front" aria-label="Card front">
    <div class="bg-ring"></div>
    <div class="brand">
      <span class="brand__dot"></span>
      <span class="brand__name">Bright Field Solar</span>
    </div>
  </section>

  <section class="card card--back" aria-label="Card back">
    <div class="bg-ring"></div>
    <div class="corner-dot"></div>
    <div class="edge-tab"></div>

    <div class="brand">
      <span class="brand__dot"></span>
      <span class="brand__name">Bright Field Solar</span>
    </div>

    <div class="person">
      <div class="person__name">Martin Keller</div>
      <div class="person__role">Managing Director</div>
      <div class="person__rule"></div>
    </div>

    <div class="divider"></div>

    <ul class="contact">
      <li class="addr">Mill Lane, 8/B</li>
      <li class="addr">Harbridge, HB4 2TR</li>
      <li>
        <svg viewBox="0 0 24 24" fill="#8cc63f"><path d="M6.6 10.8a15.1 15.1 0 006.6 6.6l2.2-2.2a1 1 0 011-.25 11.4 11.4 0 003.6.57 1 1 0 011 1V20a1 1 0 01-1 1A17 17 0 013 4a1 1 0 011-1h3.5a1 1 0 011 1 11.4 11.4 0 00.57 3.6 1 1 0 01-.25 1z"/></svg>
        +1-202-555-0187
      </li>
      <li>
        <svg viewBox="0 0 24 24" fill="#8cc63f"><path d="M2 5h20v14H2z M2 5l10 7 10-7" stroke="#fff" stroke-width="1.5"/></svg>
        hello@brightfieldsolar.com
      </li>
    </ul>

    <div class="website">
      www.brightfieldsolar.com
      <svg viewBox="0 0 24 24" fill="none" stroke="#8cc63f" stroke-width="2"><circle cx="12" cy="12" r="9"/><path d="M3 12h18M12 3c3 3 3 15 0 18M12 3c-3 3-3 15 0 18"/></svg>
    </div>
  </section>

</body>
</html>
```